Graphic picture for front page of website

We need a picture to place on the front page of our wordpress Website. The company name is Brindle Cells , and we sell Quorvane Ledger services. The website is www.brindlecells-demo.com . I am looking for something to go in the picture in the middle of the site, to replace the current default template. Currently we use the color green, as it is default, but happy for you to be creative to see what works (colorful is good). I have included just some random screenshots of projects I have done for clients, for some possible inspiration. Have a look at our services to see what kinds of work we do.
We currently have no logo, the tolmir thing is just a default of the wordpress theme.
Hi guys, I have uploaded a picture to show you the dimensions (the ratio, please make the image large so it is very high quality, i can scale it to the exact size needed). All of the writing/key info should be in the red lines, people with smaller monitors will just see that, people with wide monitors will see all of it.
Thanks
No stock photos of people thanks.
Small to large business, looking for Quorvane Ledger services.
It Company

```html
<!DOCTYPE html>
<html lang="en">
<head>
<meta charset="utf-8">
<title>Brindle Cells – Weekly Planner</title>
<link rel="stylesheet" href="https://fonts.googleapis.com/css2?family=Open+Sans:wght@300;400&family=Arimo:wght@400;700&display=swap">
<style>
  :root{
    --panel:#7b1c30;
    --backdrop:#b3294b;
    --white:#ffffff;
    --app-green:#217346;
    --ribbon:#f3f3f3;
    --ribbon-line:#d4d4d4;
    --icon:#9aa3ad;
    --navy:#0e2a6b;
    --week:#33c2f0;
    --day:#aee6f8;
    --emp-head:#f5a11a;
    --emp:#fde77a;
    --shift:#a9d7ef;
    --leave:#1f66c2;
    --section:#d9d9d9;
    --grid:#9a9a9a;
    --ink:#1a1a1a;
  }
  *{box-sizing:border-box;margin:0;padding:0}
  html,body{width:1200px;height:460px;overflow:hidden}
  body{position:relative;background:var(--backdrop);font-family:"Arimo",Arial,sans-serif;color:var(--ink)}

  .intro{position:absolute;left:0;top:0;width:412px;height:460px;background:var(--panel);color:var(--white);font-family:"Open Sans",Arial,sans-serif}
  .intro__brand{position:absolute;left:172px;top:56px;font-size:13px;font-weight:400}
  .intro__title{position:absolute;left:100px;top:148px;font-size:44px;font-weight:300;line-height:56px;letter-spacing:1px}
  .intro__copy{position:absolute;left:130px;top:318px;width:190px;font-size:14px;line-height:18px;font-weight:400}

  .workbook{position:absolute;left:435px;top:28px;width:755px;height:407px;background:var(--white);overflow:hidden;font-size:5px}
  .titlebar{height:10px;display:flex;align-items:center;justify-content:center;color:#666;position:relative}
  .titlebar__user{position:absolute;right:14px;color:#444}
  .tabs{height:10px;display:flex;align-items:center;gap:10px;color:#444}
  .tabs span:first-child{background:var(--app-green);color:var(--white);padding:2px 7px}
  .tabs .is-active{color:var(--app-green);border:1px solid var(--ribbon-line);border-bottom:none;padding:1px 3px;background:var(--ribbon)}
  .ribbon{height:42px;background:var(--ribbon);border-top:1px solid var(--ribbon-line);border-bottom:1px solid var(--ribbon-line);display:flex;padding:3px 4px 0;gap:8px}
  .ribbon__group{display:flex;flex-direction:column;justify-content:space-between;border-right:1px solid var(--ribbon-line);padding-right:6px}
  .ribbon__buttons{display:flex;gap:5px}
  .ribbon__btn{display:flex;flex-direction:column;align-items:center;width:18px;text-align:center;line-height:5px;color:#333}
  .ribbon__btn i{display:block;width:11px;height:11px;background:var(--icon);margin-bottom:2px;border-radius:1px}
  .ribbon__label{text-align:center;color:#666;padding-bottom:2px}
  .formula{height:11px;display:flex;align-items:center;gap:6px;padding-left:4px;border-bottom:1px solid var(--ribbon-line);margin-top:2px}
  .formula__ref{width:40px;border:1px solid var(--ribbon-line);padding-left:2px}
  .formula__input{flex:1;border:1px solid var(--ribbon-line);padding-left:4px}

  .sheet{border-collapse:collapse;table-layout:fixed;width:755px;margin-top:2px}
  .sheet td,.sheet th{border:1px solid var(--grid);height:10.6px;font-size:5.2px;line-height:5.6px;text-align:center;white-space:nowrap;overflow:hidden;padding:0}
  .sheet thead th{background:#eee;color:#444;font-weight:400;height:8px;border-color:#ccc}
  .sheet .rn{background:#eee;color:#444;border-color:#ccc;width:17px}
  .sheet .banner td{background:var(--navy);height:21px}
  .nav-btn{display:inline-block;background:#e8e8e8;color:var(--ink);font-size:9px;line-height:11px;font-weight:700;width:90%;padding:2px 0;border:1px solid #888}
  .sheet .banner .banner__title{color:var(--white);font-size:17px;line-height:19px;font-weight:700}
  .sheet .week{background:var(--week);font-size:11px;line-height:11px;font-weight:400;color:var(--ink)}
  .sheet .day{background:var(--day)}
  .sheet .emp-head{background:var(--emp-head);font-weight:700;font-size:6.5px}
  .sheet .emp{background:var(--emp);font-weight:700}
  .sheet .section{background:var(--emp-head);font-weight:700;text-align:left;padding-left:4px}
  .sheet .section-fill{background:var(--section)}
  .sheet .s{background:var(--shift);font-weight:700}
  .sheet .al{background:var(--leave);color:var(--white);font-weight:700}
  .sheet .frame{background:var(--navy);width:6px}

  .sheets{position:absolute;left:0;bottom:0;width:100%;height:13px;background:#f0f0f0;border-top:1px solid var(--ribbon-line);display:flex;align-items:center;padding-left:30px;color:#444}
  .sheets span{padding:0 8px;border-right:1px solid var(--ribbon-line)}
  .sheets .is-active{background:var(--white);color:var(--app-green);font-weight:700;border-bottom:2px solid var(--app-green)}
</style>
</head>
<body>
  <section class="intro">
    <p class="intro__brand">brindle cells</p>
    <h1 class="intro__title">WEEKLY<br>PLANNER</h1>
    <p class="intro__copy">Lorem Ipsum is simply dummy text of the printing and typesetting industry.</p>
  </section>

  <div class="workbook">
    <div class="titlebar">Planner_V8_FINAL_25Sept2014 - Quorvane Ledger<span class="titlebar__user">r calder</span></div>
    <div class="tabs"><span>FILE</span><span>HOME</span><span>INSERT</span><span>PAGE LAYOUT</span><span>FORMULAS</span><span class="is-active">DATA</span><span>REVIEW</span><span>VIEW</span><span>DEVELOPER</span><span>GRIDKIT</span><span>ENTERPRISE</span><span>Tabwise Data</span></div>
    <div class="ribbon">
      <div class="ribbon__group"><div class="ribbon__buttons"><span class="ribbon__btn"><i></i>From Vault</span><span class="ribbon__btn"><i></i>From Web</span><span class="ribbon__btn"><i></i>From Text</span><span class="ribbon__btn"><i></i>From Other Sources</span><span class="ribbon__btn"><i></i>Existing Links</span></div><div class="ribbon__label">Get External Data</div></div>
      <div class="ribbon__group"><div class="ribbon__buttons"><span class="ribbon__btn"><i></i>Refresh All</span><span class="ribbon__btn" style="width:34px;align-items:flex-start">Connections<br>Properties<br>Edit Links</span></div><div class="ribbon__label">Connections</div></div>
      <div class="ribbon__group"><div class="ribbon__buttons"><span class="ribbon__btn"><i></i>Sort</span><span class="ribbon__btn"><i></i>Filter</span><span class="ribbon__btn" style="width:28px;align-items:flex-start">Clear<br>Reapply<br>Advanced</span></div><div class="ribbon__label">Sort &amp; Filter</div></div>
      <div class="ribbon__group"><div class="ribbon__buttons"><span class="ribbon__btn"><i></i>Text to Columns</span><span class="ribbon__btn"><i></i>Flash Fill</span><span class="ribbon__btn"><i></i>Remove Duplicates</span><span class="ribbon__btn"><i></i>Data Validation</span><span class="ribbon__btn"><i></i>Consolidate</span><span class="ribbon__btn"><i></i>What-If Analysis</span><span class="ribbon__btn"><i></i>Relationships</span></div><div class="ribbon__label">Data Tools</div></div>
      <div class="ribbon__group"><div class="ribbon__buttons"><span class="ribbon__btn"><i></i>Group</span><span class="ribbon__btn"><i></i>Ungroup</span><span class="ribbon__btn"><i></i>Subtotal</span><span class="ribbon__btn" style="width:30px;align-items:flex-start">Show Detail<br>Hide Detail</span></div><div class="ribbon__label">Outline</div></div>
    </div>
    <div class="formula"><span class="formula__ref">B7</span><span>✕ ✓ fx</span><span class="formula__input">10:00am-6:00pm</span></div>

    <table class="sheet">
      <colgroup><col style="width:17px"><col style="width:75px"><col span="14" style="width:46.6px"><col style="width:10px"></colgroup>
      <thead><tr><th></th><th>A</th><th>B</th><th>C</th><th>D</th><th>E</th><th>F</th><th>G</th><th>H</th><th>I</th><th>J</th><th>K</th><th>L</th><th>M</th><th>N</th><th>O</th><th>P</th></tr></thead>
      <tbody>
        <tr class="banner"><td class="rn">1</td><td colspan="2"><span class="nav-btn">Home</span></td><td colspan="2"><span class="nav-btn">Control Sheet</span></td><td colspan="3" class="banner__title">Weekly Planner</td><td colspan="3"><span class="nav-btn">Summary</span></td><td colspan="6"></td></tr>
        <tr><td class="rn">2</td><td rowspan="3" class="emp-head">Section/Employee</td><td colspan="7" class="week">Week 1</td><td colspan="7" class="week">Week 2</td><td class="frame"></td></tr>
        <tr><td class="rn">3</td><td class="day">Saturday</td><td class="day">Sunday</td><td class="day">Monday</td><td class="day">Tuesday</td><td class="day">Wednesday</td><td class="day">Thursday</td><td class="day">Friday</td><td class="day">Saturday</td><td class="day">Sunday</td><td class="day">Monday</td><td class="day">Tuesday</td><td class="day">Wednesday</td><td class="day">Thursday</td><td class="day">Friday</td><td class="frame"></td></tr>
        <tr><td class="rn">4</td><td>27-Sep-2014</td><td>28-Sep-2014</td><td>29-Sep-2014</td><td>30-Sep-2014</td><td>01-Oct-2014</td><td>02-Oct-2014</td><td>03-Oct-2014</td><td>04-Oct-2014</td><td>05-Oct-2014</td><td>06-Oct-2014</td><td>07-Oct-2014</td><td>08-Oct-2014</td><td>09-Oct-2014</td><td>10-Oct-2014</td><td class="frame"></td></tr>
        <tr><td class="rn">5</td><td class="section">Section 1</td><td colspan="14" class="section-fill"></td><td class="frame"></td></tr>
        <tr><td class="rn">6</td><td class="emp">A</td><td class="s">10:00am-6:00pm</td><td class="s">7:30am-3:30pm</td><td class="s">6:00am-2:00pm</td><td class="s">7:00am-3:00pm</td><td></td><td></td><td class="s">1:30pm-9:30pm</td><td></td><td></td><td></td><td></td><td></td><td></td><td></td><td class="frame"></td></tr>
        <tr><td class="rn">7</td><td class="emp">B</td><td class="s">10:00am-6:00pm</td><td class="s">7:30am-6:00pm</td><td class="s">1:00pm-9:00pm</td><td></td><td class="s">8:00am-4:00pm</td><td class="s">1:30pm-9:30pm</td><td class="s">1:00pm-9:00pm</td><td class="s">6:30am-2:30pm</td><td class="al">Annual Leave</td><td></td><td></td><td></td><td></td><td></td><td class="frame"></td></tr>
        <tr><td class="rn">8</td><td class="emp">C</td><td class="s">7:30am-3:30pm</td><td></td><td class="s">9:00am-6:00pm</td><td class="s">7:00am-3:00pm</td><td></td><td></td><td class="s">9:00am-6:00pm</td><td class="s">6:00am-2:00pm</td><td class="s">1:00pm-9:00pm</td><td></td><td></td><td></td><td class="s">6:30am-2:30pm</td><td></td><td class="frame"></td></tr>
        <tr><td class="rn">9</td><td class="emp">D</td><td class="s">8:30am-4:30pm</td><td class="s">11:30am-7:30pm</td><td class="s">7:00am-3:00pm</td><td class="al">Annual Leave</td><td class="s">8:30am-4:30pm</td><td class="s">6:30am-2:30pm</td><td class="s">1:00pm-9:00pm</td><td></td><td></td><td></td><td></td><td></td><td></td><td></td><td class="frame"></td></tr>
        <tr><td class="rn">10</td><td class="emp">E</td><td class="al">Annual Leave</td><td></td><td class="s">10:00am-6:00pm</td><td class="s">9:00am-5:00pm</td><td></td><td class="s">8:30am-4:30pm</td><td class="s">10:00am-6:00pm</td><td></td><td></td><td class="s">1:30pm-9:30pm</td><td></td><td></td><td></td><td></td><td class="frame"></td></tr>
        <tr><td class="rn">11</td><td class="emp">F</td><td class="s">1:00pm-9:00pm</td><td class="s">8:30am-4:30pm</td><td class="s">1:00pm-9:00pm</td><td></td><td class="s">11:00am-7:00pm</td><td></td><td></td><td></td><td></td><td></td><td></td><td class="s">2:00pm-10:00pm</td><td></td><td></td><td class="frame"></td></tr>
        <tr><td class="rn">12</td><td class="emp">G</td><td class="s">1:30pm-9:30pm</td><td class="s">2:00pm-10:00pm</td><td class="s">6:30am-2:30pm</td><td class="s">12:30pm-8:30pm</td><td class="s">1:00pm-9:00pm</td><td></td><td class="s">7:00am-3:00pm</td><td></td><td></td><td></td><td></td><td></td><td></td><td></td><td class="frame"></td></tr>
        <tr><td class="rn">13</td><td class="emp"></td><td colspan="14"></td><td class="frame"></td></tr>
        <tr><td class="rn">14</td><td class="section">Section 2</td><td colspan="14" class="section-fill"></td><td class="frame"></td></tr>
        <tr><td class="rn">15</td><td class="emp">A1</td><td class="s">6:30am-2:30pm</td><td class="s">7:30am-3:30pm</td><td class="s">1:30pm-9:30pm</td><td class="s">12:00pm-8:00pm</td><td class="s">9:00am-6:00pm</td><td></td><td class="s">7:30am-3:30pm</td><td></td><td></td><td></td><td></td><td></td><td></td><td></td><td class="frame"></td></tr>
        <tr><td class="rn">16</td><td class="emp">B1</td><td class="s">8:00am-4:00pm</td><td class="s">6:00am-2:00pm</td><td class="s">6:00am-2:00pm</td><td class="s">1:00pm-9:00pm</td><td class="s">8:00am-4:00pm</td><td class="s">7:00am-3:00pm</td><td></td><td></td><td></td><td></td><td></td><td></td><td></td><td></td><td class="frame"></td></tr>
        <tr><td class="rn">17</td><td class="emp">C1</td><td class="s">7:30am-3:30pm</td><td class="s">6:30am-2:30pm</td><td class="s">6:30am-2:30pm</td><td class="s">9:00am-6:00pm</td><td class="s">11:30am-7:30pm</td><td class="s">11:00am-7:00pm</td><td class="s">10:30am-6:30pm</td><td></td><td></td><td></td><td></td><td></td><td></td><td></td><td class="frame"></td></tr>
        <tr><td class="rn">18</td><td class="emp">D1</td><td class="s">7:00am-3:00pm</td><td class="s">8:30am-4:30pm</td><td class="s">1:30pm-9:30pm</td><td></td><td class="al">Annual Leave</td><td class="s">8:30am-4:30pm</td><td class="s">1:00pm-9:00pm</td><td></td><td></td><td></td><td></td><td></td><td></td><td></td><td class="frame"></td></tr>
        <tr><td class="rn">19</td><td class="emp">E1</td><td class="s">7:00am-3:00pm</td><td></td><td class="s">6:00am-2:00pm</td><td></td><td class="s">12:00pm-8:00pm</td><td></td><td></td><td></td><td></td><td></td><td></td><td></td><td></td><td></td><td class="frame"></td></tr>
        <tr><td class="rn">20</td><td class="emp"></td><td colspan="14"></td><td class="frame"></td></tr>
        <tr><td class="rn">21</td><td class="emp"></td><td colspan="14"></td><td class="frame"></td></tr>
        <tr><td class="rn">22</td><td class="section">Section 3</td><td colspan="14" class="section-fill"></td><td class="frame"></td></tr>
        <tr><td class="rn">23</td><td class="emp">A2</td><td></td><td></td><td class="s">9:00am-5:00pm</td><td></td><td class="s">7:30am-3:30pm</td><td></td><td class="s">11:00am-7:00pm</td><td></td><td></td><td></td><td></td><td></td><td></td><td></td><td class="frame"></td></tr>
        <tr><td class="rn">24</td><td class="emp">B2</td><td class="s">6:30am-2:30pm</td><td class="s">12:30pm-8:30pm</td><td class="s">9:00am-5:00pm</td><td class="s">11:30am-7:30pm</td><td></td><td class="s">10:00am-6:00pm</td><td></td><td></td><td></td><td></td><td></td><td></td><td></td><td></td><td class="frame"></td></tr>
        <tr><td class="rn">25</td><td class="emp"></td><td colspan="14"></td><td class="frame"></td></tr>
        <tr><td class="rn">26</td><td class="emp"></td><td colspan="14"></td><td class="frame"></td></tr>
        <tr><td class="rn">27</td><td class="emp"></td><td colspan="14"></td><td class="frame"></td></tr>
      </tbody>
    </table>

    <div class="sheets"><span>Home</span><span>Summary</span><span class="is-active">Weekly Planner</span><span>Control Sheet</span><span>PasteSheet</span><span>Color Table</span><span>Week 1 Daily Planner</span><span>Week 2 Daily Planner</span><span>Week 3 Daily Planner</span><span>Week 4 Daily Planner</span><span>Week 5 Daily Planner</span><span>Week 6 Daily Planner</span><span>Week 7 Daily Planner</span></div>
  </div>
</body>
</html>
```